Progressive Architecture and Urban Planning Studio - Stationery Design

The Kestrel Collective: a small boutique Architectural and Urban Planning Studio based in Natal/ RN, Brazil, about to open branches in South Africa and West Africa, established to provide high quality, innovative design and personal client service for projects worldwide. Our approach to Architecture: Minimal - Less is More, so to speak, but with an edge! Strive to produce "clean" projects - stripped of all that can be stripped, no excesses. Got our Logo right here with Pixel Harbor, and hope to do the same with our stationery (were informed that includes business cards, letterhead and envelopes). Since we'll be using two clour schemes, we want at least one using a black background (business card). We'll also allow manipulation of our logo if it helps the final design. Good Luck!

Font styles to use
Other font styles liked:
• Nexa

Colors

Designer to choose colors to be used in the design.

Requirements
Must have
• Business Cards/ Letterheads with the following address:
Rua Olavo Pereira 2741, Vale Dourado, Natal/RN
Should be able to edit it.

```html
<!DOCTYPE html>
<html lang="en">
<head>
<meta charset="UTF-8">
<title>The Kestrel Collective – Business Card</title>
<link rel="stylesheet" href="https://fonts.googleapis.com/css2?family=Montserrat:wght@400&family=Arimo:wght@400;700&display=swap">
<style>
  :root {
    --backdrop: #e6e6e6;
    --card-dark: #363636;
    --card-light: #ffffff;
    --brand-red: #e30613;
    --ink: #111111;
    --ink-soft: #333333;
    --on-dark: #ffffff;
  }
  * { margin: 0; padding: 0; box-sizing: border-box; }
  html, body {
    width: 910px;
    height: 1200px;
    overflow: hidden;
    background: var(--backdrop);
  }
  .sheet { position: relative; width: 910px; height: 1200px; }

  .card {
    position: absolute;
    left: 47px;
    width: 817px;
    height: 530px;
  }
  .card--front { top: 43px; background: var(--card-dark); }
  .card--back  { top: 625px; background: var(--card-light); }

  .wordmark {
    position: absolute;
    display: flex;
    align-items: center;
    font-family: "Montserrat", sans-serif;
    font-weight: 400;
    text-transform: uppercase;
    white-space: nowrap;
  }
  .wordmark__square { background: var(--brand-red); flex: none; }

  .card--front .wordmark {
    left: 0; right: 0; top: 234px;
    justify-content: center;
    gap: 34px;
    color: var(--on-dark);
    font-size: 30px;
    letter-spacing: 0.3em;
  }
  .card--front .wordmark__square { width: 60px; height: 60px; }

  .card--back .wordmark {
    right: 24px; top: 50px;
    gap: 20px;
    color: var(--ink);
    font-size: 17px;
    letter-spacing: 0.3em;
  }
  .card--back .wordmark__square { width: 40px; height: 40px; }

  .contact {
    position: absolute;
    left: 36px;
    top: 243px;
    font-family: "Arimo", sans-serif;
  }
  .contact__name { font-size: 30px; font-weight: 400; color: #000; line-height: 1.1; }
  .contact__role { margin-top: 6px; font-size: 22px; color: var(--brand-red); }
  .contact__details { margin-top: 33px; margin-left: 4px; font-size: 17px; color: var(--ink-soft); line-height: 1.25; }
  .contact__address { margin-bottom: 5px; }
  .contact__group + .contact__group { margin-top: 13px; }
  .contact__label { color: var(--brand-red); font-weight: 700; margin-right: 6px; }
</style>
</head>
<body>
<main class="sheet">
  <section class="card card--front" aria-label="Business card front">
    <div class="wordmark">
      <span class="wordmark__square" aria-hidden="true"></span>
      <span class="wordmark__name">The Kestrel Collective</span>
    </div>
  </section>

  <section class="card card--back" aria-label="Business card back">
    <div class="wordmark">
      <span class="wordmark__square" aria-hidden="true"></span>
      <span class="wordmark__name">The Kestrel Collective</span>
    </div>

    <div class="contact">
      <h1 class="contact__name">Name</h1>
      <p class="contact__role">Architectural and Urban Planning</p>
      <div class="contact__details">
        <p class="contact__address">Rua Olavo Pereira 2741, Vale Dourado, Natal/RN</p>
        <div class="contact__group">
          <p><span class="contact__label">Tel :</span>+000 000 0000</p>
          <p><span class="contact__label">Mob :</span>+000 000 0000</p>
        </div>
        <div class="contact__group">
          <p><span class="contact__label">E-mail :</span>name@kestrelcollective.com</p>
          <p><span class="contact__label">Web :</span>www.kestrelcollective.com</p>
        </div>
      </div>
    </div>
  </section>
</main>
</body>
</html>
```